Thornwell Building Company - advertisement poster

I am looking to print some canvas signs to advertise my general contracting company, Thornwell Building Company. The sign will measure 6' long x 3' high so the size should match that ratio. I already have a logo icon, which is the Letter 'A' and some trees that I would like to incorporate, see attached. I would also like the to have the following information listed:
1) phone number: 472-318-6095
2) email: thornwellbuildingcompany@mailvistra.net
3) website: thornwellbuildingcompany.com
4) Lic#5386204
5) I want to use this text: "BUILD WITH THE T-CREW!"

The ad should be relatively simple and clean. Black and Green are my company colors. I am open to creative ideas!

Target Market(s)

People looking to renovate their homes

Industry/Entity Type

Construction

Colors
59FF00
82FF00
B8FF75
E3FFCB
F4FFEA

Requirements
Must have
• Must have my company logo
Should not have
• No photos or complex graphics

```html
<!DOCTYPE html>
<html lang="en">
<head>
<meta charset="UTF-8">
<title>Thornwell Building Company – Sign</title>
<link rel="stylesheet" href="https://fonts.googleapis.com/css2?family=Arimo:wght@400;700&family=Source+Sans+3:wght@400&family=Orbitron:wght@700&display=swap">
<style>
  :root {
    --page-bg: #d4eaf5;
    --navy: #002334;
    --green: #70b244;
    --white: #ffffff;
    --sky-deep: #0a5fb0;
    --sky-light: #2aa3dc;
  }
  * { margin: 0; padding: 0; box-sizing: border-box; }
  html, body { width: 1200px; height: 1200px; overflow: hidden; background: var(--page-bg); }
  .sign {
    position: absolute; left: 92px; top: 346px; width: 1016px; height: 508px;
    background: var(--navy); overflow: hidden;
  }
  .sign-graphics { position: absolute; inset: 0; width: 1016px; height: 508px; }
  .brand { position: absolute; left: 30px; top: 30px; width: 124px; text-align: center; }
  .brand-mark { width: 22px; height: 22px; background: var(--green); margin: 0 auto 10px; }
  .brand-name {
    font-family: "Arimo", sans-serif; font-weight: 700; color: var(--white);
    font-size: 15px; letter-spacing: 0.5px; line-height: 1.1;
  }
  .brand-sub {
    font-family: "Arimo", sans-serif; font-weight: 700; color: var(--white);
    font-size: 6.5px; letter-spacing: 2.4px; margin-top: 2px;
  }
  .headline { position: absolute; left: 30px; top: 156px; font-family: "Arimo", sans-serif; line-height: 1; }
  .headline-top { color: var(--white); font-size: 45px; font-weight: 400; letter-spacing: 0.5px; }
  .headline-accent { color: var(--green); font-size: 46px; font-weight: 700; margin-top: 4px; }
  .license {
    position: absolute; right: 28px; top: 14px;
    font-family: "Arimo", sans-serif; color: var(--white); font-size: 31px;
  }
  .contacts { position: absolute; left: 30px; top: 377px; list-style: none; }
  .contact { display: flex; align-items: center; height: 25px; margin-bottom: 12px; }
  .contact-icon {
    width: 25px; height: 25px; border-radius: 4px; background: var(--green);
    display: flex; align-items: center; justify-content: center; margin-right: 13px;
  }
  .contact-icon svg { width: 16px; height: 16px; }
  .contact-text { font-family: "Source Sans 3", sans-serif; color: var(--white); font-size: 20px; }
</style>
</head>
<body>
  <div class="sign">
    <svg class="sign-graphics" viewBox="0 0 1016 508" aria-hidden="false">
      <defs>
        <linearGradient id="skyline-tone" x1="0" y1="0" x2="1" y2="1">
          <stop offset="0" stop-color="var(--sky-deep)" style="stop-color:#0a5fb0"/>
          <stop offset="0.55" stop-color="#1a8fd2"/>
          <stop offset="1" stop-color="#b9d4e6"/>
        </linearGradient>
      </defs>
      <circle class="photo-ring" cx="722" cy="42" r="320" fill="#70b244"/>
      <circle class="photo-ring-gap" cx="728" cy="48" r="309" fill="#002334"/>
      <circle class="photo-area" cx="731" cy="52" r="304" fill="url(#skyline-tone)" role="img" aria-label="Photo of glass office towers seen from below against a blue sky"/>
      <path class="license-tab" d="M748,0 H1016 V70 H790 A42,42 0 0 1 748,28 Z" fill="#70b244"/>
      <path class="wave-navy" d="M0,362 C180,295 420,280 580,345 C680,385 760,425 850,408 C930,392 985,330 1016,195 V508 H0 Z" fill="#002334"/>
      <path class="wave-white-left" d="M-10,360 C160,296 330,284 470,312" fill="none" stroke="#ffffff" stroke-width="11"/>
      <path class="wave-white-right" d="M600,385 C760,440 920,400 1025,305" fill="none" stroke="#ffffff" stroke-width="11"/>
      <path class="wave-green" d="M-10,345 C200,268 420,280 570,342 C660,380 735,428 825,428 C920,428 985,378 1025,335" fill="none" stroke="#70b244" stroke-width="12"/>
    </svg>

    <div class="brand">
      <div class="brand-mark"></div>
      <div class="brand-name">THORNWELL</div>
      <div class="brand-sub">BUILDING COMPANY</div>
    </div>

    <div class="license">Lic#5386204</div>

    <h1 class="headline">
      <div class="headline-top">BUILD WITH THE</div>
      <div class="headline-accent">T-CREW</div>
    </h1>

    <ul class="contacts">
      <li class="contact">
        <span class="contact-icon">
          <svg viewBox="0 0 16 16"><path d="M4 1.5l2.2 3-1.3 1.6c.8 1.8 2.2 3.2 4 4l1.6-1.3 3 2.2-1.2 2.5C7 13.8 2.2 9 1.5 3.3z" fill="#002334"/></svg>
        </span>
        <span class="contact-text">472-318-6095</span>
      </li>
      <li class="contact">
        <span class="contact-icon">
          <svg viewBox="0 0 16 16"><rect x="1.5" y="3.5" width="13" height="9" fill="none" stroke="#002334" stroke-width="1.3"/><path d="M1.5 3.5l6.5 5 6.5-5M1.5 12.5l5-4.5M14.5 12.5l-5-4.5" fill="none" stroke="#002334" stroke-width="1.1"/></svg>
        </span>
        <span class="contact-text">thornwellbuildingcompany@mailvistra.net</span>
      </li>
      <li class="contact">
        <span class="contact-icon">
          <svg viewBox="0 0 16 16"><circle cx="8" cy="8" r="6.3" fill="none" stroke="#002334" stroke-width="1.3"/><ellipse cx="8" cy="8" rx="2.8" ry="6.3" fill="none" stroke="#002334" stroke-width="1.1"/><path d="M1.7 8h12.6M2.6 5h10.8M2.6 11h10.8" stroke="#002334" stroke-width="1"/></svg>
        </span>
        <span class="contact-text">thornwellbuildingcompany.com</span>
      </li>
    </ul>
  </div>
</body>
</html>
```